Business Card Design - front and back

Residential real estate agent looking for a an emphasis on my first name (last name is hard to spell).  Would love the slogan "It's more than a contract" on the card.  Simple, easy to read business card that makes people want to pick it up and remember it.  The Bright Gable Properties has to be on the front of card but does not need to be the emphasis.  Prefer locations on the back.  Would love a home on it.  Looking for simply elegant in the card that shows I am a non-complicated, warm, honest real estate agent.
NEED ONE OF MY PICTURES ON THE CARD.  LEAVING WHICH ONE UP TO THE DESIGNER.

Industry/Entity Type
Real Estate
Contact Information for Business Card
Marla Quist, Broker Associate, Bright Gable Properties, 727-555-0148 cell, callmemarla@example.net, listedwithmarla.example, Bright Gable Properties locations: 48215 Pellory Blvd Ste 101, Tampa, FL  33999, 2918 Vossin Ct Ste 101, New Port Richey, FL  34999
I NEED THIS DOUBLE SIDED - THE SELECTION BELOW WILL NOT ALLOW IT?
Requirements
Must have
- Emphasis on my first name
a home in it
LOVE Gloria Padgett's logo which sits on the left side in the margin at
http://gloriapadgett.sampleagentsite.example/
Something with that idea is exactly what I am looking for.
Nice to have
- Nice script that is readable.
Should not have
- I am looking for something simple

```html
<!DOCTYPE html>
<html lang="en">
<head>
<meta charset="utf-8">
<title>Marla Quist – Business Card, Front and Back</title>
<link href="https://fonts.googleapis.com/css2?family=Open+Sans:wght@300;400;600;700&display=swap" rel="stylesheet">
<style>
  :root {
    --backdrop: #e4e4e2;
    --card-blue: #1a7aa6;
    --card-dark: #2f2e2f;
    --card-white: #ffffff;
    --ink-dark: #2f2e2f;
    --ink-light: #f2f2f2;
    --shadow: rgba(0, 0, 0, 0.18);
  }
  * { box-sizing: border-box; margin: 0; padding: 0; }
  html, body {
    width: 1200px; height: 873px; overflow: hidden;
    background: var(--backdrop);
    font-family: "Open Sans", Arial, sans-serif;
  }
  .canvas {
    position: relative; width: 1200px; height: 873px;
    display: flex; align-items: center; justify-content: center; gap: 40px;
  }
  .card {
    position: relative; width: 520px; height: 297px; overflow: hidden;
    box-shadow: 0 6px 18px var(--shadow);
    background: var(--card-white);
  }
  .band { position: absolute; left: 0; width: 100%; }

  /* Front */
  .front .band-blue { top: 0; height: 190px; background: var(--card-blue); }
  .front .band-white { top: 190px; height: 34px; background: var(--card-white); }
  .front .band-dark { top: 224px; height: 73px; background: var(--card-dark); }

  .company-name {
    color: var(--card-white); font-weight: 300; letter-spacing: 0.5px;
    text-transform: uppercase; white-space: nowrap;
  }
  .front .company-name {
    position: absolute; left: 26px; top: 148px; font-size: 22px;
    display: flex; align-items: center; gap: 10px;
  }
  .company-mark { width: 12px; height: 12px; border: 2px solid var(--card-white); }

  .stripe-row {
    position: absolute; left: 26px; right: 26px; top: 0; height: 34px;
    display: flex; align-items: center; font-size: 10px; color: var(--ink-dark);
  }
  .stripe-row .phone { display: flex; align-items: center; gap: 6px; }
  .stripe-row .title {
    margin-left: 18px; color: var(--card-blue); font-weight: 600;
    text-transform: uppercase; letter-spacing: 0.4px;
  }
  .agent-name {
    margin-left: auto; font-size: 19px; text-transform: uppercase;
    letter-spacing: 0.5px; color: var(--ink-dark); font-weight: 400;
  }
  .agent-name .first { color: var(--card-blue); font-weight: 700; }

  .contact-grid {
    position: absolute; left: 26px; right: 26px; top: 0; height: 73px;
    display: flex; align-items: center; gap: 34px;
    color: var(--ink-light); font-size: 9.5px; line-height: 1.45;
  }
  .contact-item { display: flex; gap: 7px; align-items: flex-start; }
  .contact-item svg { flex: none; margin-top: 2px; }
  .contact-web { margin-left: auto; }

  /* Back */
  .back .band-dark { top: 0; height: 200px; background: var(--card-dark); }
  .back .band-white { top: 200px; height: 22px; background: var(--card-white); }
  .back .band-blue { top: 222px; height: 75px; background: var(--card-blue); }
  .back .company-name {
    position: absolute; left: 0; right: 0; top: 150px; font-size: 24px;
    display: flex; justify-content: center; align-items: center; gap: 10px;
  }
  .slogan {
    position: absolute; left: 0; right: 0; top: 244px; text-align: center;
    color: var(--ink-light); font-size: 11px; font-weight: 400; letter-spacing: 0.3px;
  }
</style>
</head>
<body>
<main class="canvas">

  <section class="card front" aria-label="Card front">
    <div class="band band-blue">
      <div class="company-name"><span class="company-mark"></span>Bright Gable Properties</div>
    </div>
    <div class="band band-white">
      <div class="stripe-row">
        <span class="phone">
          <svg width="7" height="11" viewBox="0 0 7 11" aria-hidden="true"><rect x="0.5" y="0.5" width="6" height="10" rx="1" fill="none" stroke="#2f2e2f"/><rect x="2.5" y="8.3" width="2" height="1" fill="#2f2e2f"/></svg>
          +1-727-555-0148
        </span>
        <span class="title">Broker Associate</span>
        <span class="agent-name"><span class="first">Marla</span> Quist</span>
      </div>
    </div>
    <div class="band band-dark">
      <div class="contact-grid">
        <div class="contact-item">
          <svg width="10" height="10" viewBox="0 0 10 10" aria-hidden="true"><path d="M1 5 L5 1 L9 5 V9 H1 Z" fill="#f2f2f2"/></svg>
          <span>48215 Pellory Blvd<br>Ste 101, Tampa, FL 33999</span>
        </div>
        <div class="contact-item">
          <svg width="10" height="10" viewBox="0 0 10 10" aria-hidden="true"><path d="M1 5 L5 1 L9 5 V9 H1 Z" fill="#f2f2f2"/></svg>
          <span>2918 Vossin Ct Ste 101,<br>New Port Richey, FL 34999</span>
        </div>
        <div class="contact-item contact-web">
          <svg width="10" height="20" viewBox="0 0 10 20" aria-hidden="true"><rect x="0.5" y="1.5" width="9" height="6" fill="none" stroke="#f2f2f2"/><path d="M0.5 1.5 L5 5 L9.5 1.5" fill="none" stroke="#f2f2f2"/><rect x="0.5" y="12" width="9" height="7" fill="none" stroke="#f2f2f2"/></svg>
          <span>callmemarla@example.net<br>listedwithmarla.example</span>
        </div>
      </div>
    </div>
  </section>

  <section class="card back" aria-label="Card back">
    <div class="band band-dark">
      <div class="company-name"><span class="company-mark"></span>Bright Gable Properties</div>
    </div>
    <div class="band band-white"></div>
    <div class="band band-blue"></div>
    <p class="slogan">Its more than a contract...</p>
  </section>

</main>
</body>
</html>
```